Three Ebook Covers for Short Stories

Three Ebook cover designs for 3 short stories (all linked) psychological thriller. I like clean crisp images. Perhaps with an imagine of eyes/part of face - white woman, 29, thin, brown eyes, short bob hair. I like gritty, moody, raw type of images. I dont mind the same image being used on three covers providing there are differences (ie slight variation in colour of book). Colours I prefer red, burgundy, black, grey, white. My website shows off the type of colours I prefer. www.lydiakbarnes-author.net
Branding is important.

Target Market(s)

Adult. Moth in Attic, Lost Field, type of readers.

Industry/Entity Type

Book Publisher

Font styles to use
Sans Serif
Other font styles liked:
• fonts used on thriller novels

Requirements
Must have
• Author Name: Lydia K Barnes
• Short Story as Part of Title
• Short Story 1: Title - First Crow
• Short Story 2: Title - Second Crow
• Short Story 3: Title - Third Crow
• Branding is important so they must look like they are a set.
• A font which is aligned to thriller type novels
• Colours aligned to my website - red, burgundy, white, grey, black.
Nice to have
• I don't mind a black and white type photo imagine.
Should not have
• n/a

```html
<!DOCTYPE html>
<html lang="en">
<head>
<meta charset="utf-8">
<title>First Crow — Lydia K Barnes</title>
<link rel="stylesheet" href="https://fonts.googleapis.com/css2?family=Raleway:wght@300&display=swap">
<style>
  :root {
    --ink-red: #e04a2c;
    --panel-top: #a3301a;
    --panel-mid: #86200f;
    --panel-bottom: #5e130a;
    --photo-light: #c2523a;
    --photo-mid: #8c2a1a;
    --photo-dark: #3a0d06;
  }
  * { margin: 0; padding: 0; box-sizing: border-box; }
  html, body { width: 800px; height: 1200px; overflow: hidden; background: var(--panel-bottom); }
  .cover {
    position: relative;
    width: 800px;
    height: 1200px;
    overflow: hidden;
    font-family: "Raleway", sans-serif;
    font-weight: 300;
    color: var(--ink-red);
    background: radial-gradient(ellipse at 40% 40%, var(--panel-top) 0%, var(--panel-mid) 50%, var(--panel-bottom) 100%);
  }
  .cover-photo {
    position: absolute;
    left: 0; top: 0;
    width: 800px;
    height: 440px;
    background:
      radial-gradient(ellipse 260px 140px at 62% 55%, var(--photo-light) 0%, transparent 70%),
      linear-gradient(90deg, var(--photo-dark) 0%, var(--photo-mid) 30%, var(--photo-mid) 75%, var(--photo-dark) 100%);
  }
  .series-label {
    position: absolute;
    left: 55px;
    top: 470px;
    font-size: 34px;
    letter-spacing: 1px;
    text-transform: uppercase;
  }
  .story-title {
    position: absolute;
    left: 48px;
    top: 520px;
    font-size: 218px;
    line-height: 176px;
    letter-spacing: 4px;
    text-transform: uppercase;
  }
  .story-title span { display: block; }
  .author-name {
    position: absolute;
    left: 52px;
    top: 918px;
    font-size: 92px;
    line-height: 96px;
    letter-spacing: 3px;
    text-transform: uppercase;
  }
  .author-name span { display: block; }
</style>
</head>
<body>
  <main class="cover">
    <div class="cover-photo" role="img" aria-label="Close-up photograph of a young woman's eyes under a dark fringe, tinted red"></div>
    <p class="series-label">Short Story 1</p>
    <h1 class="story-title"><span>First</span><span>Crow</span></h1>
    <p class="author-name"><span>Lydia K</span><span>Barnes</span></p>
  </main>
</body>
</html>
```